packing for cake and sweet

we need packing design for cake box.
I attached some nice packing from other shop like :
Bruma and velmont for examples.

I attached the logo.
you can make packing with any colors you choose.

box size :
length : 30 cm
Width : 30 cm
Height : 15 cm

this shops have very good design :
https://www.quorvell.co.uk/hot-chocolate/discover-hot-chocolate/all-hot-chocolate

Industry/Entity Type

food

Font styles to use
Other font styles liked:
• same our logo already attached.

```html
<!DOCTYPE html>
<html lang="en">
<head>
<meta charset="utf-8">
<title>Calvaine – Cake Box Lid Designs</title>
<link rel="stylesheet" href="https://fonts.googleapis.com/css2?family=Cinzel:wght@400&family=Montserrat:wght@400&display=swap">
<style>
  :root {
    --canvas: #ffffff;
    --mist: #e6e8e8;
    --ink: #231f20;
    --ink-soft: #4a4a4a;
    --blush: #f1cfc6;
    --blush-deep: #eab3a5;
    --gold: #e9cf95;
    --gold-pale: #f7ecd3;
  }
  * { box-sizing: border-box; margin: 0; padding: 0; }
  html, body {
    width: 1200px; height: 1200px; overflow: hidden;
    background: var(--canvas);
  }
  .board { position: relative; width: 1200px; height: 1200px; }

  .lid {
    position: absolute; top: 435px; width: 467px; height: 330px; overflow: hidden;
  }
  .lid--blush { left: 88px; background: var(--mist); }
  .lid--gold { left: 652px; background: var(--canvas); }

  .artwork { position: absolute; }

  /* watercolour lilies */
  .artwork--lily-left {
    left: 0; top: 0; width: 112px; height: 292px;
    background: linear-gradient(160deg, var(--blush-deep) 0%, var(--blush) 70%, rgba(241,207,198,0.6) 100%);
    border-radius: 0 46% 40% 0;
  }
  .artwork--lily-right {
    left: 355px; top: 50px; width: 112px; height: 224px;
    background: linear-gradient(200deg, var(--blush-deep) 0%, var(--blush) 70%, rgba(241,207,198,0.6) 100%);
    border-radius: 46% 0 0 40%;
  }

  /* gold line wreath */
  .artwork--wreath-top {
    left: 80px; top: 0; width: 330px; height: 118px;
    background: linear-gradient(180deg, var(--gold-pale) 0%, var(--gold) 100%);
    border-radius: 40% 40% 45% 45%;
    opacity: 0.75;
  }
  .artwork--wreath-left {
    left: 0; top: 105px; width: 115px; height: 115px;
    background: linear-gradient(135deg, var(--gold) 0%, var(--gold-pale) 100%);
    border-radius: 50% 30% 50% 50%;
    opacity: 0.75;
  }
  .artwork--wreath-bottom {
    left: 140px; top: 212px; width: 327px; height: 118px;
    background: linear-gradient(0deg, var(--gold-pale) 0%, var(--gold) 100%);
    border-radius: 45% 45% 40% 40%;
    opacity: 0.75;
  }
  .artwork--wreath-right {
    left: 380px; top: 150px; width: 87px; height: 90px;
    background: linear-gradient(225deg, var(--gold) 0%, var(--gold-pale) 100%);
    border-radius: 40% 50% 50% 50%;
    opacity: 0.75;
  }

  .wordmark {
    position: absolute; left: 0; right: 0; text-align: center;
    font-family: "Cinzel", serif; font-weight: 400;
    color: var(--ink); line-height: 1; font-size: 42px; letter-spacing: 0.5px;
  }
  .lid--blush .wordmark { top: 150px; }
  .lid--gold .wordmark { top: 137px; }

  .tagline {
    position: absolute; left: 0; right: 0; text-align: center;
    font-family: "Montserrat", sans-serif; font-size: 8px;
    letter-spacing: 1.6px; color: var(--ink-soft); line-height: 1;
  }
  .lid--blush .tagline { top: 207px; }
  .lid--gold .tagline { top: 193px; }
</style>
</head>
<body>
<main class="board">

  <section class="lid lid--blush">
    <div class="artwork artwork--lily-left" role="img" aria-label="Watercolour blush lily petals with fine navy line work"></div>
    <div class="artwork artwork--lily-right" role="img" aria-label="Watercolour blush lily blossom with fine navy line work"></div>
    <h1 class="wordmark">Calvaine</h1>
    <p class="tagline">Lorem ipsum Lorem ipsum</p>
  </section>

  <section class="lid lid--gold">
    <div class="artwork artwork--wreath-top" role="img" aria-label="Gold line drawing of blossoms and leafy branches arching above the name"></div>
    <div class="artwork artwork--wreath-left" role="img" aria-label="Gold line drawing of a leafy spray at the left"></div>
    <div class="artwork artwork--wreath-right" role="img" aria-label="Gold line drawing of a leafy spray at the right"></div>
    <div class="artwork artwork--wreath-bottom" role="img" aria-label="Gold line drawing of blossoms and leafy branches curving below the name with gold speckles"></div>
    <h1 class="wordmark">Calvaine</h1>
    <p class="tagline">Lorem ipsum Lorem ipsum</p>
  </section>

</main>
</body>
</html>
```